Kestrel Summit 2019 Enemies of the End-Times Church Flyer

We want a church conference flyer designed. We are looking for a professional, yet catchy design that uses our brand colors and logo creatively while communicating key information of the event effectively. <br/>The flyer must include all of the following:<br/>Title: Kestrel Summit 2019<br/>Topic: The Enemies of The End-Times Church <br/>Subtitles: <br/> -How the antichrist raises an army by social behavior engineering. <br/>-How the architects of modern social constructs escaped the church's radar. <br/>-The Holy Spirit's end-times agenda:<br/> The Knock-Out Punch!<br/>Speaker: Prophet Marcus Toliver <br/>Dates/time: December 27, 28 & 29 at 6pm<br/>Location: Halvorn Community Center <br/> 241 Pellham Street <br/> Portland, ME 04102<br/>Contact info: phone: 207-555-0148 <br/>email: contact@brookmeadow.example <br/> www.vutel.example<br/>*The flyer must also include a picture of the speaker and our Vutel logo <br/>Thanks, we look forward to seeing what you come up with!

Colors

Designer to choose colors to be used in the design.

Requirements
Must have
• The flyer must include all of the following:
• Title: Kestrel Summit 2019
• Topic: The Enemies of The End-Times Church
• Subtitles:
• -How the antichrist raises an army by social behavior engineering.
• -How the architects of modern social constructs escaped the church's radar.
• -The Holy Spirit's end-times agenda:
• The Knock-Out Punch!
• Speaker: Prophet Marcus Toliver
• Dates/time: December 27, 28 & 29 at 6pm
• Location: Halvorn Community Center
• 241 Pellham Street
• Portland, ME 04102
• Contact info: phone: 207-555-0148
• email: contact@brookmeadow.example
• www.vutel.example
• *The flyer must also include a picture of the speaker and our Vutel logo
Should not have
• Pictures of crosses or church buildings

```html
<!DOCTYPE html>
<html lang="en">
<head>
<meta charset="utf-8">
<title>Kestrel Summit 2019 – Flyer</title>
<link rel="stylesheet" href="https://fonts.googleapis.com/css2?family=Cinzel:wght@400;600;700&display=swap">
<style>
  :root {
    --navy: #0f2a57;
    --navy-deep: #0a1f45;
    --navy-mid: #1a4a8c;
    --orange: #e8551a;
    --orange-bright: #f2661f;
    --panel-grey: #e4e4e4;
    --ring-grey: #9a9a9a;
    --page-bg: #ebe8e4;
    --white: #ffffff;
    --serif: "Cinzel", "Trajan Pro", Georgia, serif;
  }
  * { box-sizing: border-box; margin: 0; padding: 0; }
  html, body { width: 1200px; height: 900px; overflow: hidden; background: var(--page-bg); }
  .flyer {
    position: absolute; left: 295px; top: 20px;
    width: 609px; height: 860px;
    background: var(--white);
    font-family: var(--serif);
    color: var(--navy);
    overflow: hidden;
    box-shadow: 0 4px 18px rgba(0,0,0,.18);
  }
  .flyer > * { position: absolute; }
  .speaker-photo {
    left: 0; top: 0; width: 609px; height: 380px;
    background: linear-gradient(90deg, #ffffff 0%, #f1efec 30%, #c9c2b9 55%, #7d6e62 78%, #5b4c44 100%);
    -webkit-mask-image: linear-gradient(to bottom, #000 62%, transparent 92%);
    mask-image: linear-gradient(to bottom, #000 62%, transparent 92%);
  }
  .backdrop { left: 0; top: 0; width: 609px; height: 860px; }
  .brand { left: 16px; top: 44px; font-size: 48px; font-weight: 400; color: var(--navy); letter-spacing: 1px; line-height: 1; }
  .topic { left: 8px; top: 206px; font-size: 30px; line-height: 38px; letter-spacing: .5px; }
  .topic .accent { color: var(--orange); }
  .badge {
    left: 57px; top: 308px; width: 196px; height: 196px; border-radius: 50%;
    background: radial-gradient(circle at 40% 30%, var(--orange-bright) 0%, var(--orange) 60%, #c8430f 100%);
    border: 4px solid var(--ring-grey);
    box-shadow: 0 10px 8px -6px rgba(0,0,0,.45);
    display: flex; flex-direction: column; align-items: center; justify-content: center;
    color: var(--white); text-align: center; line-height: 1;
  }
  .badge-line1 { font-size: 30px; }
  .badge-line2 { font-size: 22px; margin-top: 2px; }
  .badge-year { font-size: 32px; margin-top: 4px; }
  .event-date { left: 313px; top: 382px; font-size: 19px; color: var(--navy); white-space: nowrap; }
  .venue { left: 337px; top: 420px; display: flex; align-items: center; gap: 9px; }
  .venue-text { font-size: 12.5px; line-height: 15px; color: var(--navy); }
  .section-head {
    left: 4px; top: 574px; width: 601px;
    display: flex; align-items: center; gap: 8px;
    font-size: 19px; font-weight: 400; color: var(--orange); white-space: nowrap;
  }
  .section-head::before, .section-head::after { content: ""; flex: 1; height: 2px; background: var(--orange); }
  .agenda {
    left: 5px; top: 603px; width: 601px; height: 178px;
    border: 3px solid var(--navy); border-radius: 4px;
    padding: 3px;
  }
  .agenda-inner {
    width: 100%; height: 100%; border-radius: 3px;
    background: linear-gradient(100deg, var(--navy-deep) 0%, var(--navy-mid) 70%, var(--navy-deep) 100%);
    padding: 18px 6px 0 10px;
    list-style: none;
  }
  .agenda-item {
    display: flex; gap: 8px; color: var(--white);
    font-size: 14.5px; line-height: 16px; margin-bottom: 14px;
  }
  .agenda-item::before {
    content: ""; flex: none; width: 10px; height: 10px; margin-top: 3px;
    border-radius: 50%; background: var(--orange);
  }
  .contact-box {
    left: 9px; top: 796px; width: 345px; height: 51px;
    border: 2px solid var(--navy); border-radius: 3px;
    font-size: 12.5px; color: var(--navy);
  }
  .contact-phone { position: absolute; left: 27px; top: 9px; }
  .contact-icons { position: absolute; left: 140px; top: 10px; display: flex; gap: 3px; }
  .contact-icons span { width: 11px; height: 11px; border-radius: 50%; background: var(--orange); }
  .contact-web { position: absolute; left: 208px; top: 9px; font-size: 12px; }
  .contact-email { position: absolute; left: 63px; top: 26px; color: var(--orange); font-size: 12px; }
  .speaker-credit { right: 70px; top: 810px; text-align: right; }
  .speaker-name { font-size: 14px; color: var(--navy); white-space: nowrap; }
  .speaker-role { font-size: 7px; color: var(--orange); margin-top: 1px; }
  .care-emblem { left: 550px; top: 800px; width: 44px; height: 42px; border-radius: 50%; background: var(--orange); }
  .base-strip { left: 0; top: 855px; width: 609px; height: 5px; background: var(--orange); }
</style>
</head>
<body>
<main class="flyer">
  <div class="speaker-photo" role="img" aria-label="Portrait of Prophet Marcus Toliver in front of bookshelves"></div>

  <svg class="backdrop" viewBox="0 0 609 860" aria-hidden="true">
    <path d="M0 548 Q240 328 609 306 L609 860 L0 860 Z" fill="var(--panel-grey)"/>
    <path d="M0 520 Q232 300 609 292 L609 306 Q240 328 0 548 Z" fill="var(--orange)"/>
  </svg>

  <div class="brand">VUTEL</div>

  <h1 class="topic"><span class="accent">The Enemies</span> of The<br>End-Times Church</h1>

  <div class="badge">
    <span class="badge-line1">Kestrel</span>
    <span class="badge-line2">Summit</span>
    <span class="badge-year">2019</span>
  </div>

  <p class="event-date">December 27, 28 &amp; 29 at 6pm</p>

  <div class="venue">
    <svg width="40" height="40" viewBox="0 0 40 40" aria-hidden="true">
      <circle cx="20" cy="20" r="20" fill="var(--navy)"/>
      <path d="M20 10 a7 7 0 0 1 7 7 c0 5 -7 13 -7 13 s-7 -8 -7 -13 a7 7 0 0 1 7 -7z" fill="var(--white)"/>
      <circle cx="20" cy="17" r="2.6" fill="var(--navy)"/>
    </svg>
    <p class="venue-text">Halvorn Community<br>Center 241 Pellham<br>Street Portland, ME 04102</p>
  </div>

  <h2 class="section-head">The Enemies of The End-Times Church</h2>

  <div class="agenda">
    <ul class="agenda-inner">
      <li class="agenda-item">How the antichrist raises an army by social behavior engineering.</li>
      <li class="agenda-item">How the architects of modern social constructs escaped the church's radar.</li>
      <li class="agenda-item">The Holy Spirit's end-times agenda:</li>
      <li class="agenda-item">The Knock-Out Punch!</li>
    </ul>
  </div>

  <div class="contact-box">
    <span class="contact-phone">207-555-0148</span>
    <span class="contact-icons" aria-hidden="true"><span></span><span></span><span></span></span>
    <span class="contact-web">www.vutel.example</span>
    <span class="contact-email">contact@brookmeadow.example</span>
  </div>

  <div class="speaker-credit">
    <div class="speaker-name">Prophet Marcus Toliver</div>
    <div class="speaker-role">Speaker</div>
  </div>

  <div class="care-emblem" role="img" aria-label="Emblem of joined hands"></div>

  <div class="base-strip"></div>
</main>
</body>
</html>
```